Footpath/Sidewalk inspection company needs poster

We need a poster for an upcoming technical conference. Our company has a specialist footpath/sidewalk inspection system. The poster is to be mounted on the outside of our booth to get the interest of potential customers.
I would like the main part of the poster to have the image "P3060103" but transparent or faded. The large main text should say "Do you need to know where every individual fault is on your footpath network?"
A smaller part of the poster should have the map "Zoom Out" with an expanding view to the "Zoom in" image. This part should have small text "Whakatane District, 15,700 faults recorded"
Road Engineers
It Company

```html
<!DOCTYPE html>
<html lang="en">
<head>
<meta charset="utf-8">
<title>Kerbline Surveys Ltd – Footpath Fault Poster</title>
<link rel="stylesheet" href="https://fonts.googleapis.com/css2?family=Oswald:wght@400;500;700&family=Montserrat:wght@400&display=swap">
<style>
  :root {
    --page: #ffffff;
    --orange: #ef6a1c;
    --orange-deep: #e2531a;
    --orange-light: #f7a45a;
    --peach: #fbd8b4;
    --cream: #fdebd6;
    --ink: #1c1c1c;
    --asphalt: #8d8a88;
    --asphalt-warm: #c99a86;
    --grass: #5f7a3a;
    --frame: #ffffff;
    --connector: #7d7d7d;
  }
  html, body {
    margin: 0;
    width: 1200px;
    height: 1200px;
    overflow: hidden;
    background: var(--page);
  }
  .poster {
    position: absolute;
    left: 234px;
    top: 24px;
    width: 742px;
    height: 1142px;
    overflow: hidden;
    background: var(--orange);
  }
  .poster-art {
    position: absolute;
    inset: 0;
    width: 742px;
    height: 1142px;
  }
  .brand {
    position: absolute;
    left: 40px;
    top: 58px;
    width: 320px;
    text-align: center;
    font-family: 'Oswald', sans-serif;
    color: var(--ink);
  }
  .brand-name {
    margin: 0;
    font-weight: 500;
    font-size: 34px;
    line-height: 1.05;
    letter-spacing: 1px;
    text-transform: uppercase;
  }
  .brand-name .mark {
    display: inline-block;
    width: 20px;
    height: 20px;
    border-radius: 50%;
    background: var(--orange);
    margin-right: 10px;
    vertical-align: 4px;
  }
  .brand-url {
    margin: 10px 0 0;
    font-family: 'Montserrat', sans-serif;
    font-size: 12.5px;
    letter-spacing: 0.8px;
    color: var(--orange-deep);
  }
  .headline {
    font-family: 'Oswald', sans-serif;
    fill: var(--ink);
  }
  .headline .emphasis { font-weight: 700; }
  .map-label {
    font-family: 'Oswald', sans-serif;
    font-weight: 500;
    fill: #ffffff;
  }
</style>
</head>
<body>
  <main class="poster">
    <svg class="poster-art" viewBox="0 0 742 1142" xmlns="http://www.w3.org/2000/svg">
      <defs>
        <linearGradient id="footpathTone" x1="0" y1="0" x2="1" y2="0">
          <stop offset="0" stop-color="#e69a82"/>
          <stop offset="0.35" stop-color="#b49a92"/>
          <stop offset="0.7" stop-color="#8f8b8a"/>
          <stop offset="1" stop-color="#9a9a7a"/>
        </linearGradient>
        <linearGradient id="vergeTone" x1="0" y1="0" x2="0" y2="1">
          <stop offset="0" stop-color="#4f7032"/>
          <stop offset="1" stop-color="#a59a6e"/>
        </linearGradient>
        <linearGradient id="topBand" x1="0" y1="0" x2="1" y2="1">
          <stop offset="0" stop-color="#f59a4a"/>
          <stop offset="1" stop-color="#e4531a"/>
        </linearGradient>
        <linearGradient id="mapNear" x1="0" y1="0" x2="1" y2="1">
          <stop offset="0" stop-color="#3a4a40"/>
          <stop offset="0.3" stop-color="#5c6b52"/>
          <stop offset="1" stop-color="#4c6238"/>
        </linearGradient>
        <linearGradient id="mapFar" x1="0" y1="0" x2="0" y2="1">
          <stop offset="0" stop-color="#2f5f78"/>
          <stop offset="0.12" stop-color="#3f6a3a"/>
          <stop offset="1" stop-color="#2d4a22"/>
        </linearGradient>
        <filter id="frameShadow" x="-10%" y="-10%" width="130%" height="130%">
          <feDropShadow dx="2" dy="4" stdDeviation="4" flood-opacity="0.35"/>
        </filter>
      </defs>

      <!-- faded footpath photograph area -->
      <g role="img" aria-label="Faded photograph of a cracked asphalt footpath beside a kerb and hedge">
        <rect x="0" y="150" width="742" height="860" fill="url(#footpathTone)"/>
        <polygon points="600,150 742,150 742,1000 660,1000 620,560 560,330" fill="url(#vergeTone)" opacity="0.55"/>
        <rect x="0" y="150" width="742" height="860" fill="#f07a3a" opacity="0.12"/>
      </g>

      <!-- top orange facets -->
      <polygon points="384,0 742,0 742,220 560,190 480,160 384,120" fill="url(#topBand)"/>
      <polygon points="560,0 742,0 742,120 640,60" fill="#e8481a" opacity="0.6"/>
      <polygon points="0,144 310,220 480,170 470,240 310,285 0,210" fill="#f07a30" opacity="0.85"/>
      <polygon points="0,210 310,285 470,240 470,265 310,305 0,240" fill="#f5a06a" opacity="0.5"/>

      <!-- white brand panel -->
      <polygon points="0,0 384,0 384,176 310,222 0,144" fill="#ffffff"/>

      <!-- lower orange facets -->
      <polygon points="0,800 300,880 300,1142 0,1142" fill="var(--orange)" opacity="0.9"/>
      <polygon points="0,860 200,900 160,1142 0,1142" fill="var(--orange-deep)" opacity="0.7"/>
      <polygon points="0,1020 130,1142 0,1142" fill="#f2894a"/>
      <polygon points="626,950 742,880 742,1000 660,1000" fill="var(--orange)"/>
      <polygon points="378,990 742,960 742,1142 460,1142" fill="var(--orange)"/>
      <polygon points="378,1000 560,1010 600,1142 440,1142" fill="#d9bca6" opacity="0.85"/>
      <polygon points="500,1030 742,990 742,1142 620,1142" fill="var(--peach)"/>
      <polygon points="560,1050 742,1070 742,1142 600,1142" fill="var(--cream)"/>

      <!-- headline -->
      <g class="headline">
        <text x="144" y="385" font-size="60" font-weight="500" textLength="301" lengthAdjust="spacingAndGlyphs">Do you need</text>
        <text x="118" y="457" font-size="60" font-weight="500" textLength="512" lengthAdjust="spacingAndGlyphs">to know where every</text>
        <text class="emphasis" x="144" y="536" font-size="62" textLength="472" lengthAdjust="spacingAndGlyphs">INDIVIDUAL FAULT</text>
        <text x="205" y="600" font-size="60" font-weight="500" textLength="242" lengthAdjust="spacingAndGlyphs">is on your</text>
        <text x="118" y="668" font-size="60" font-weight="500" textLength="470" lengthAdjust="spacingAndGlyphs">footpath network?</text>
      </g>

      <!-- zoom connector -->
      <polygon points="242,976 275,742 275,960" fill="var(--connector)" opacity="0.85"/>

      <!-- zoomed-out map -->
      <g filter="url(#frameShadow)">
        <rect x="90" y="916" width="288" height="180" fill="var(--frame)"/>
      </g>
      <rect x="102" y="926" width="263" height="162" fill="url(#mapFar)" role="img" aria-label="Satellite map of the Whakatane District coastline, zoomed out"/>

      <!-- zoomed-in map -->
      <g filter="url(#frameShadow)">
        <rect x="275" y="742" width="351" height="218" fill="var(--frame)"/>
      </g>
      <rect x="287" y="752" width="326" height="194" fill="url(#mapNear)" role="img" aria-label="Satellite map of Whakatane town streets with recorded footpath faults marked"/>
      <rect x="334" y="924" width="178" height="16" fill="#2a2a2a" opacity="0.75"/>
      <text class="map-label" x="338" y="936" font-size="8.6" textLength="170" lengthAdjust="spacingAndGlyphs">WHAKATANE DISTRICT, 15,700 FAULTS RECORDED</text>
    </svg>

    <header class="brand">
      <h1 class="brand-name"><span class="mark"></span>Kerbline Surveys Ltd</h1>
      <p class="brand-url">www.kerblinesurveys.co.nz</p>
    </header>
  </main>
</body>
</html>
```